Stickers to put on my honeyglasses

Stickers for my honey glasses.
Only a single sticker on the front. Same should have a stripe on the top side which goes above the lid to show if the glass was opened.
Size of the main part should be 55mm high and max. 100 mm wide.
The stripe on the top should be 70mm long.
I added a Picture of another producer which uses the same glass as I do.
I should say: 'e Maringer Glas Hunneg'. which means 'another glass of honey. 'Hunneg' should be mainly visible and therefore very large. 'e Maringer Glas' should be less visible and therefore smaller above the 'Hunneg'
- It needs to contain the quantity : '500gr'
- It needs to contain my Name and address: 'Jos Maringer, 14, rue Pierre Faber, L-7590 Miersch' (This should be small and not to visible)
- It needs to conatin a validity Line: ´Am beschte virum:` (With enough space so I can add a date by hand)
- It needs to say: 'dréchen, kill andäischterstockéieren' (to store it dry cold and dark)

```html
<!DOCTYPE html>
<html lang="lb">
<head>
<meta charset="utf-8">
<title>Hunneg – Glas Etikett</title>
<link rel="stylesheet" href="https://fonts.googleapis.com/css2?family=Fraunces:opsz,wght@9..144,700&family=Outfit:ital,wght@0,400;0,500;1,400&display=swap">
<style>
  :root {
    --backdrop: #bfbfbf;
    --label-black: #0d0d0d;
    --label-black-soft: #1c1a16;
    --gold: #d6a766;
    --gold-light: #f0c88a;
    --gold-deep: #a8763c;
    --write-field: #ffffff;
  }
  html, body {
    margin: 0;
    width: 1200px;
    height: 1200px;
    overflow: hidden;
    background: var(--backdrop);
  }
  .canvas {
    width: 1200px;
    height: 1200px;
    display: block;
  }
  .label-body { fill: url(#label-fill); }
  .label-border { fill: none; stroke: var(--gold); stroke-width: 2; }
  .sans { font-family: "Outfit", sans-serif; }
  .producer-line { font-size: 27px; font-weight: 500; fill: var(--gold-light); }
  .product-name {
    font-family: "Fraunces", serif;
    font-weight: 700;
    font-size: 124px;
    fill: url(#gold-fill);
  }
  .quantity { font-size: 27px; font-weight: 500; fill: var(--gold-light); }
  .best-before { font-size: 23px; font-weight: 500; fill: var(--gold-light); }
  .date-field { fill: var(--write-field); }
  .storage-note { font-size: 21px; font-style: italic; fill: var(--gold); }
  .producer-address { font-size: 10px; fill: var(--gold-deep); }
</style>
</head>
<body>
<svg class="canvas" viewBox="0 0 1200 1200" xmlns="http://www.w3.org/2000/svg">
  <defs>
    <radialGradient id="label-fill" cx="50%" cy="65%" r="60%">
      <stop offset="0" stop-color="var(--label-black-soft)"/>
      <stop offset="1" stop-color="var(--label-black)"/>
    </radialGradient>
    <linearGradient id="gold-fill" x1="0" y1="0" x2="1" y2="0">
      <stop offset="0" stop-color="var(--gold-deep)"/>
      <stop offset="0.5" stop-color="var(--gold-light)"/>
      <stop offset="1" stop-color="var(--gold-deep)"/>
    </linearGradient>
  </defs>

  <g class="sticker">
    <path class="label-body" role="img" aria-label="Black label background with a faint golden honeycomb pattern"
          d="M553,200 H647 V540 H840 L905,720 L840,900 H360 L295,720 L360,540 H553 Z"/>
    <path class="label-border"
          d="M565,200 V552 H372 L309,720 L372,888 H828 L891,720 L828,552 H635 V200"/>

    <text class="sans producer-line" x="600" y="594" text-anchor="middle">e Maringer Glas Hunneg</text>
    <text class="product-name" x="600" y="705" text-anchor="middle">Hunneg</text>
    <text class="sans quantity" x="600" y="750" text-anchor="middle">500gr</text>

    <text class="sans best-before" x="608" y="806" text-anchor="end">Am beschte virum:</text>
    <rect class="date-field" x="620" y="783" width="202" height="32" rx="16"/>

    <text class="sans storage-note" x="600" y="853" text-anchor="middle">dréchen, kill andäischterstockéieren</text>
    <text class="sans producer-address" x="600" y="877" text-anchor="middle">Jos Maringer, 14, rue Pierre Faber, L-7590 Miersch</text>
  </g>
</svg>
</body>
</html>
```